Make a medical leaflet for my patients undergoing ankle blocks

I have a very boring text only leaflet I would like to turn into a professional appealing medical leaflet to give to my patients. I would like to get this onto two pages of a4 if possible and its intended for electronic distribution mainly.
This will be for patients so it must be professional.
It must also contain a copyright logo on it and my name near the start (Dr Tobias Renner) so my colleagues can't use it easily.
Target Market(s)
Patients undergoing surgery
Industry/Entity Type
Medical
Other font styles liked:
- no idea, you tell me
Requirements
Must have
- the information contained on the attachment
- look professional
- a copyright on it
Nice to have
- the fernbrook clinic logo
Should not have
- Any spelling, grammatical or linguistic errors
- Any font less than size 12

```html
<!DOCTYPE html>
<html lang="en">
<head>
<meta charset="utf-8">
<title>Ankle Block – Patient Information</title>
<link href="https://fonts.googleapis.com/css2?family=Lato:wght@300;400;700&family=Titillium+Web:wght@400;600&display=swap" rel="stylesheet">
<style>
  :root{
    --navy:#3a2d6c;
    --navy-deep:#2f2560;
    --teal:#45c1c4;
    --page:#ebebed;
    --stage:#d6d6d8;
    --ink:#26262e;
    --white:#ffffff;
    --band:linear-gradient(90deg,var(--navy) 0%,#3d4c86 45%,var(--teal) 100%);
  }
  *{box-sizing:border-box;margin:0;padding:0}
  html,body{width:1200px;height:879px;overflow:hidden;background:var(--stage)}
  body{position:relative;font-family:"Lato",Arial,sans-serif;color:var(--ink)}
  .page{position:absolute;top:48px;width:553px;height:780px;background:var(--page);overflow:hidden}
  .page--front{left:34px}
  .page--back{left:608px}
  .abs{position:absolute}
  .heading{font-family:"Titillium Web",Arial,sans-serif;font-weight:600}

  /* brand */
  .brand__name{font-family:"Lato",Arial,sans-serif;font-weight:400;color:var(--navy);font-size:19px;letter-spacing:.2px;padding-bottom:3px;border-bottom:1px solid var(--navy);white-space:nowrap}
  .brand__group{font-family:"Lato",Arial,sans-serif;font-weight:400;color:var(--navy);font-size:9px;white-space:nowrap;margin-top:6px;text-align:center}
  .brand__group b{font-weight:400;font-size:12px}
  .doctor{left:358px;top:20px;width:174px;height:24px;border:1.5px solid var(--navy);color:var(--navy);font-size:15px;text-align:center;line-height:21px}

  /* hero */
  .hero{left:0;top:73px;width:553px;height:213px;background:linear-gradient(100deg,#3c5d8e 0%,#4f8fae 50%,#56b7c2 100%)}
  .hero__tag{left:0;top:73px;width:170px;height:93px}
  .hero__title{left:22px;top:100px;color:var(--white);font-size:20px}
  .hero__text{color:var(--white);font-weight:700;font-size:10.5px;line-height:13.4px}
  .hero__intro{left:196px;top:88px;width:334px}

  /* section bands */
  .band{left:0;width:553px;background:var(--band);color:var(--white)}
  .band__title{font-size:19px;line-height:1}
  .band__icon{stroke:var(--white);fill:none;stroke-width:2}

  .benefits{left:50px;top:334px;list-style:none}
  .benefits li{font-size:11.3px;font-weight:400;line-height:18px;white-space:nowrap;color:var(--ink)}
  .benefits .num{display:inline-block;width:30px;color:var(--teal);font-weight:700;font-size:12px}
  .benefits strong{font-weight:700;font-size:12.5px}

  /* risks */
  .timeline{left:159px;top:501px;width:1.5px;height:204px;background:var(--navy)}
  .timeline__dot{left:154px;width:11px;height:11px;border-radius:50%;background:var(--navy)}
  .risk__label{left:58px;color:var(--navy);font-weight:700;font-size:12.5px;line-height:15px}
  .risk__icon{left:22px;stroke:var(--navy);fill:none;stroke-width:1.6}
  .risk__text{left:178px;width:352px;font-size:10.9px;font-weight:400;line-height:13.5px;color:var(--ink)}
  .risk__text strong{font-weight:700;font-size:12.6px;color:var(--navy-deep)}
  .options{left:178px;top:653px;list-style:none}
  .options li{color:var(--navy);font-size:13px;line-height:19px}
  .front-note{left:22px;top:722px;width:505px;font-size:10.9px;line-height:13.5px;color:var(--ink)}

  /* back page */
  .how{left:0;top:0}
  .how__title{left:88px;top:18px;color:var(--white);font-size:20px}
  .how__sub{left:88px;top:46px;color:var(--white);font-weight:700;font-size:10.4px;line-height:13.5px}
  .how__icon{left:38px;top:20px;stroke:var(--white);fill:none;stroke-width:1.8}
  .body-text{font-size:10.9px;font-weight:400;line-height:13.3px;color:var(--ink)}
  .tile{left:2px;width:56px;background:linear-gradient(180deg,var(--navy) 0%,#3f6d99 60%,var(--teal) 100%)}
  .tile svg{position:absolute;left:16px;stroke:var(--white);fill:none;stroke-width:1.8}
  .sec-title{left:64px;color:var(--navy);font-size:21px;line-height:1}
  .checks{left:76px;top:342px;width:452px;list-style:none}
  .checks li{position:relative;padding-left:14px;font-size:10.9px;font-weight:400;line-height:13.3px;color:var(--ink)}
  .checks li svg{position:absolute;left:-2px;top:1px}
  .checks strong{font-weight:700;font-size:12px}
  .alt{left:65px;top:609px;width:420px}
  .alt p{font-size:13px;line-height:15.5px;margin-bottom:4.5px;color:var(--ink)}
  .back-foot{left:0;top:714px;width:553px;height:66px;background:var(--band);color:var(--white);text-align:center;font-size:10.9px;line-height:13.3px;padding:8px 44px 0}
  .copyright{margin-top:3px;font-size:9.5px;line-height:12px;font-weight:700;letter-spacing:.2px}
</style>
</head>
<body>

<!-- ============ FRONT PAGE ============ -->
<section class="page page--front">
  <div class="abs brand" style="left:28px;top:16px">
    <div class="brand__name">Fernbrook Clinic</div>
    <div class="brand__group">part of <b>Calder Health Group</b></div>
  </div>
  <div class="abs doctor">Dr Tobias Renner</div>

  <div class="abs hero" role="img" aria-label="Photograph of surgical staff walking along a hospital corridor"></div>
  <svg class="abs hero__tag" viewBox="0 0 170 93" aria-hidden="true">
    <polygon points="0,0 124,0 170,93 0,93" fill="#3a2d6c"/>
  </svg>
  <h1 class="abs hero__title heading">Ankle block</h1>
  <p class="abs hero__text hero__intro">You are scheduled to have surgery on your foot. It is my normal practice to offer and perform (with your consent) an ankle block. This is an optional injection of numbing liquid to the nerves which supply your foot. The ankle block can be performed when you are awake, sedated or under general anaesthesia.</p>
  <p class="abs hero__text" style="left:22px;top:174px;width:510px">The ankle block can be combined with a general anaesthetic and with sedation. It can also be used to allow surgery to be performed with you wide awake in certain cases.</p>
  <p class="abs hero__text" style="left:22px;top:213px;width:510px">Having or not having an ankle block does not change the pre-operative fasting guidelines you have been given.</p>
  <p class="abs hero__text" style="left:22px;top:246px;width:510px">There is a fee for performing an ankle block. Please consult my initial introductory email and terms of business for details.</p>

  <div class="abs band" style="top:286px;height:40px">
    <svg class="abs band__icon" style="left:22px;top:9px" width="24" height="24" viewBox="0 0 24 24" aria-hidden="true">
      <path d="M3 3v18h18"/><path d="M8 16 19 5M12 5h7v7"/>
    </svg>
    <h2 class="abs band__title heading" style="left:78px;top:10px">What are the benefits</h2>
  </div>

  <ol class="abs benefits">
    <li><span class="num">1.</span>Excellent pain relief – usually <strong>10 – 14 hours</strong> (and rarely <strong>24 – 48 hours</strong>)</li>
    <li><span class="num">2.</span>Avoiding traditional painkillers which results in less post-operative nausea and vomiting</li>
    <li><span class="num">3.</span>The option to avoid a general anaesthetic (if you wish)</li>
    <li><span class="num">4.</span>A faster recovery from the general anaesthetic</li>
    <li><span class="num">5.</span>Certain surgery requires an overnight stay in hospital without an ankle block</li>
  </ol>

  <div class="abs band" style="top:432px;height:55px">
    <svg class="abs band__icon" style="left:22px;top:9px" width="28" height="26" viewBox="0 0 28 26" aria-hidden="true">
      <path d="M14 2 26 24H2Z"/><path d="M15 9l-4 7h5l-3 5"/>
    </svg>
    <h2 class="abs band__title heading" style="left:84px;top:9px">What are the risks?</h2>
    <p class="abs" style="left:83px;top:34px;font-size:11.3px">As with all injections, there is the risk of bruising, bleeding and infection.</p>
  </div>

  <div class="abs timeline"></div>

  <svg class="abs risk__icon" style="top:514px" width="22" height="20" viewBox="0 0 22 20" aria-hidden="true"><path d="M2 8c3-6 9-7 14-3l4 5-4 8H7Z"/></svg>
  <div class="abs risk__label" style="top:518px">Nerve Damage</div>
  <div class="abs timeline__dot" style="top:524px"></div>
  <p class="abs risk__text" style="top:498px">Occurs <strong>1 in 5000</strong> nerve blocks. Creates an area of numbness or <strong>weakness/paralysis in some / all the foot.</strong> The majority of nerve injuries will heal themselves within a year. There is no treatment to fix it. If the block has not worn off after <strong>72 hours</strong> please let me know.</p>

  <svg class="abs risk__icon" style="top:565px" width="18" height="30" viewBox="0 0 18 30" aria-hidden="true"><rect x="2" y="2" width="14" height="22" rx="1"/><path d="M6 8l6 6M12 8l-6 6"/></svg>
  <div class="abs risk__label" style="top:577px">Failure</div>
  <div class="abs timeline__dot" style="top:582px"></div>
  <p class="abs risk__text" style="top:567px">The success rate with ankle blocks is <strong>98 – 99%</strong>. Some blocks will fail, partially or totally. If total failure, I will discuss repeating the block with your consent.</p>

  <svg class="abs risk__icon" style="top:617px" width="22" height="22" viewBox="0 0 22 22" aria-hidden="true"><circle cx="11" cy="11" r="8"/><path d="M11 6v6M11 15v1"/></svg>
  <div class="abs risk__label" style="top:617px">Pain during<br>operation</div>
  <div class="abs timeline__dot" style="top:622px"></div>
  <p class="abs risk__text" style="top:619px">If you choose to have wide awake surgery or surgery under sedation, the surgery will stop and I will discuss three options with you:</p>
  <ul class="abs options">
    <li>more numbing liquid to be injected by the surgeon</li>
    <li>more sedation / painkiller</li>
    <li>having a general anaesthetic</li>
  </ul>

  <p class="abs front-note">If you decide to undergo surgery awake or sedated, there is a risk you will need to have a general anaesthetic if you feel pain. This is why the fasting instructions for awake surgery and general anaesthesia are the same.</p>
</section>

<!-- ============ BACK PAGE ============ -->
<section class="page page--back">
  <svg class="abs how" width="330" height="94" viewBox="0 0 330 94" aria-hidden="true">
    <polygon points="0,0 244,0 318,94 0,94" fill="#3a2d6c"/>
    <polygon points="250,0 260,0 330,94 320,94" fill="#3a2d6c"/>
  </svg>
  <svg class="abs how__icon" width="38" height="24" viewBox="0 0 38 24" aria-hidden="true">
    <path d="M2 4h7l3 12H4ZM36 4h-7l-3 12h8ZM12 6l7-2 8 3M12 15l5 4 3-2 3 2 3-4"/>
  </svg>
  <h2 class="abs how__title heading">How is it done</h2>
  <p class="abs how__sub">If you choose awake surgery or<br>surgery with sedation –</p>

  <div class="abs brand" style="left:360px;top:37px">
    <div class="brand__name">Fernbrook Clinic</div>
    <div class="brand__group">part of <b>Calder Health Group</b></div>
  </div>

  <p class="abs body-text" style="left:35px;top:102px;width:482px">Numbing liquid is injected around the nerves which supply your foot. The ankle block takes 5 – 10 minutes to perform and requires 4 – 5 injections. Approximately 10 – 20 minutes to make your foot numb to pain. I will check the ankle block is working before we start surgery using cold spray. Sensations of touch, pressure, vibration and movement will still be felt. I will use a screen so you can't see the surgery (unless you would like to see). Some patients bring headphones to block out the noise of the operation.</p>

  <div class="abs tile" style="top:192px;height:54px">
    <svg style="top:14px" width="24" height="26" viewBox="0 0 24 26" aria-hidden="true"><path d="M9 14V3a2 2 0 0 1 4 0v9l7 2-2 10H9l-6-7 3-2 3 3"/></svg>
  </div>
  <h2 class="abs sec-title heading" style="top:208px">If you choose a General anaesthetic –</h2>
  <p class="abs body-text" style="left:67px;top:238px;width:456px">I will perform the ankle block after I start the general anaesthetic. You should wake up from your surgery with a comfortable and numb foot/feet. If you wake in pain, we can repeat the ankle block or provide traditional painkillers. Whatever you choose, there will be a cannula placed in your hand and heart and oxygen monitoring throughout.</p>

  <div class="abs tile" style="top:301px;height:55px">
    <svg style="top:14px" width="24" height="28" viewBox="0 0 24 28" aria-hidden="true"><path d="M4 2l14 20M20 2 6 22"/><circle cx="5" cy="24" r="2.5"/><circle cx="19" cy="24" r="2.5"/></svg>
  </div>
  <h2 class="abs sec-title heading" style="top:312px">After surgery</h2>

  <ul class="abs checks">
    <li style="margin-bottom:8px"><svg width="11" height="11" viewBox="0 0 11 11" aria-hidden="true"><circle cx="5.5" cy="5.5" r="5.5" fill="#3a2d6c"/><path d="M3 5.6l1.8 1.8L8 4" stroke="#fff" stroke-width="1.4" fill="none"/></svg>You will go to the recovery area and then onto the ward when you are ready. It will be difficult to walk while the block is working so physiotherapists will help you first walk. If you need crutches they will teach you how to use them.</li>
    <li style="margin-bottom:8px"><svg width="11" height="11" viewBox="0 0 11 11" aria-hidden="true"><circle cx="5.5" cy="5.5" r="5.5" fill="#3a2d6c"/><path d="M3 5.6l1.8 1.8L8 4" stroke="#fff" stroke-width="1.4" fill="none"/></svg>Your foot will be numb and so you will not feel where your foot is in relation to nearby objects. As a result, it is easy to knock your foot. Please take extra care while your foot is still numb.</li>
    <li style="margin-bottom:8px"><svg width="11" height="11" viewBox="0 0 11 11" aria-hidden="true"><circle cx="5.5" cy="5.5" r="5.5" fill="#3a2d6c"/><path d="M3 5.6l1.8 1.8L8 4" stroke="#fff" stroke-width="1.4" fill="none"/></svg>As the block wears off, the foot may feel slightly painful, tingly or hot. At this point you should take your painkillers I have prescribed. Depending on your medical history you will have up to three painkillers. I would suggest to start with all three. You will also have an anti-sickness prescribed if one of the painkillers (typically codeine or morphine) makes you feel sick.</li>
    <li><svg width="11" height="11" viewBox="0 0 11 11" aria-hidden="true"><circle cx="5.5" cy="5.5" r="5.5" fill="#3a2d6c"/><path d="M3 5.6l1.8 1.8L8 4" stroke="#fff" stroke-width="1.4" fill="none"/></svg>Occasionally <strong>(1 – 2%)</strong>, pain when the block wears off will be severe. In this case contact your surgeon's secretary. We can use stronger pain medication, but there will be a charge in writing and getting the private prescription to you (please see my terms of business) via courier.</li>
  </ul>

  <div class="abs tile" style="top:570px;height:49px">
    <svg style="top:11px" width="24" height="28" viewBox="0 0 24 28" aria-hidden="true"><path d="M5 26V10M11 26V6M17 26V10"/><circle cx="5" cy="7" r="2.5"/><circle cx="11" cy="3" r="2.5"/><circle cx="17" cy="7" r="2.5"/></svg>
  </div>
  <h2 class="abs sec-title heading" style="top:582px">The alternative</h2>
  <div class="abs alt">
    <p>If you do not have an ankle block your surgery can still proceed.</p>
    <p>Post-operative pain can be managed with traditional painkillers.</p>
    <p>However, you are more likely to need an overnight stay or feel sick after the anaesthetic.</p>
  </div>

  <footer class="abs back-foot">
    <p>If you have any further questions about an ankle block I will see you the day of your surgery. Alternatively, you can request the following optional services (as mentioned in my terms of business).</p>
    <p class="copyright">© Dr Tobias Renner. All rights reserved.</p>
  </footer>
</section>

</body>
</html>
```